Best Selling Book Cover Design for Non-Fiction Adventure

Hello there!I'm looking for a gorgeous front and back book cover design worthy of a Best Seller for my book that will be published next week. It is about the story of my walk of the Sendero de Valmora, the 500-mile pilgrimage across the northern part of Spain. I've attached a detailed description along with the content for the back cover. I'm also attaching a bunch of pictures from the walk although it is not necessary to any of these. I need a cover that sells and speaks to the description, whatever you think that will be best. Book DetailsTitle: One Million StepsSubtitle: Lessons From A Legendary HikeAuthor: Ngan H. NguyenSpecifics:- The book will be 5.5" by 8.5" and 194 pages (may change slightly and we can update the spine in final revisions). - Paperback and leave space for a bar code- Will need the raw files so this can be redesigned into hardcover down the line- Bookvane book cover upload ready- Final file will also need the front cover only for e-book version- Add profile headshot (attached) to back-cover if space permits.

Target Market(s)

Those interested in adventure stories, spirituality, healing, transformation, self-actualization.

Font styles to use
Serif
Script

Colors

Designer to choose colors to be used in the design.

Requirements
Nice to have
• Potentially some of the infamous symbols of the Sendero like the seashell or yellow arrows. Maybe fog or mist over the path or village to create a mysterious feel. Not all mandatory.
• Maybe some cool blending effects of various artifacts or pictures.

```html
<!DOCTYPE html>
<html lang="en">
<head>
<meta charset="utf-8">
<title>A Thousand Dawns – Cover Wrap</title>
<link rel="stylesheet" href="https://fonts.googleapis.com/css2?family=Bebas+Neue&family=Arimo:wght@400;700&family=Libre+Baskerville&display=swap">
<style>
  :root {
    --backdrop: #4f4f4f;
    --sky-violet: #5a3150;
    --sky-rose: #8c4456;
    --sunset-orange: #ee7f2a;
    --sunset-gold: #f6b04a;
    --dune-brown: #6a3a2a;
    --shadow-brown: #2b1a17;
    --ink-light: #ffffff;
    --ink-soft: rgba(255,255,255,0.92);
    --spine-edge: rgba(0,0,0,0.28);
  }
  * { box-sizing: border-box; margin: 0; padding: 0; }
  html, body { width: 1200px; height: 800px; overflow: hidden; background: var(--backdrop); }
  .cover-wrap {
    position: absolute; left: 101px; top: 30px;
    width: 998px; height: 740px;
    display: grid; grid-template-columns: 479px 40px 479px;
    box-shadow: 0 10px 30px rgba(0,0,0,0.35);
  }
  .cover-art {
    position: absolute; inset: 0;
    background:
      radial-gradient(ellipse 60% 18% at 50% 44%, rgba(250,190,80,0.55), transparent 70%),
      linear-gradient(180deg, var(--sky-violet) 0%, var(--sky-rose) 20%, #c25a3c 33%, var(--sunset-orange) 42%, var(--sunset-gold) 46%, #b3552e 53%, var(--dune-brown) 68%, var(--shadow-brown) 100%);
  }
  .panel { position: relative; height: 100%; color: var(--ink-light); text-align: center; }
  .spine {
    position: relative; height: 100%;
    border-left: 1px solid var(--spine-edge); border-right: 1px solid var(--spine-edge);
    display: flex; flex-direction: column; align-items: center; justify-content: space-between;
    padding: 34px 0 30px;
  }
  .spine-title, .spine-author { writing-mode: vertical-rl; color: var(--ink-light); }
  .spine-title { font-family: "Bebas Neue", sans-serif; font-size: 30px; letter-spacing: 0.5px; }
  .spine-author { font-family: "Libre Baskerville", serif; font-size: 17px; }

  .back { padding: 60px 48px 0; }
  .back-title { font-family: "Bebas Neue", sans-serif; font-size: 46px; line-height: 1; }
  .back-subtitle { font-family: Arimo, sans-serif; font-size: 15px; letter-spacing: 0.5px; margin-top: 2px; text-transform: uppercase; }
  .blurb { font-family: Arimo, sans-serif; font-size: 10.5px; line-height: 1.4; color: var(--ink-soft); margin-top: 22px; }
  .blurb p + p { margin-top: 12px; }
  .headshot { width: 64px; height: 64px; border-radius: 50%; margin: 20px auto 10px; background: radial-gradient(circle at 50% 40%, #c99a7c, #5b3a2c); border: 2px solid rgba(255,255,255,0.5); }
  .bio { font-family: Arimo, sans-serif; font-size: 10.5px; line-height: 1.4; color: var(--ink-soft); }

  .front { padding: 120px 40px 0; }
  .front-title {
    font-family: "Bebas Neue", sans-serif; font-size: 118px; line-height: 0.9;
    text-shadow: 0 3px 8px rgba(0,0,0,0.35);
  }
  .front-title span { display: block; }
  .front-subtitle { font-family: Arimo, sans-serif; font-size: 27px; line-height: 1.2; margin-top: 34px; text-transform: uppercase; }
  .front-author { position: absolute; left: 0; right: 0; bottom: 70px; font-family: "Libre Baskerville", serif; font-size: 34px; }
</style>
</head>
<body>
  <main class="cover-wrap">
    <div class="cover-art" role="img" aria-label="Sunset over a wooden boardwalk leading through sand dunes and beach grass, rope railings on both sides"></div>

    <section class="panel back">
      <h2 class="back-title">A Thousand Dawns</h2>
      <p class="back-subtitle">Notes From A Wandering Season</p>
      <div class="blurb">
        <p>Stretching 500-miles across the northern part of Spain is the Sendero Francés of the Sendero de Valmora. A pilgrimage to the Spanish city of San Elio de Valmora.</p>
        <p>It was by fate that I found this path and it became one of the greatest adventures of my life. Over a million steps crossing the rugged Pyrenees and spanning undulating plains before winding through lush hillsides. The path was a unique window into historical, natural and cultural beauty, but even more than that, it was a walk into more depth within my own being. It became a journey of healing and self-discovery.</p>
        <p>The many gifts, lessons, and miracles that I came to discover along this path allowed me to see how the path mirrors our journey to any destination we have in mind. Arriving at San Elio de Valmora, I was transformed and the gifts the path brought me was more than I ever thought was possible.</p>
        <p>In this book, I tell the story of that adventure as well as the countless powerful lessons I learned in the hope that it may of service to you. May the lessons I learned shine more light on your journey to whatever destination that may be pulling at your consciousness at this moment.</p>
        <p>Buen Sendero – Good Way to You.</p>
      </div>
      <div class="headshot" role="img" aria-label="Author headshot"></div>
      <p class="bio">Thao K. Pham has built her platform of a vision-driven life after 10 years of experience working as a business strategy advisor in Summit 500 companies and at Harrowgate &amp; Partners. Combining her advisory experience with her passion for spiritual principles of success, she now empowers entrepreneurs, change-makers, and leaders to step into their truth and bring their unique vision to life. Enabling them to change their lives, revolutionize their work, create greater impact in the world.</p>
    </section>

    <aside class="spine">
      <span class="spine-title">A Thousand Dawns</span>
      <span class="spine-author">Thao K. Pham</span>
    </aside>

    <section class="panel front">
      <h1 class="front-title"><span>A</span><span>Thousand</span><span>Dawns</span></h1>
      <p class="front-subtitle">Notes From A<br>Wandering Season</p>
      <p class="front-author">Thao K. Pham</p>
    </section>
  </main>
</body>
</html>
```